Integrative Medical Practice Website Redo

I am needing to have our current website redesigned to make it a responsive website to work on smartphones.
Current website
www.brightoakfm.com
Here are several examples of what I am looking for
https://www.corvanhealth.com/
I am wanting a popup for a newsletter signup
Looking for a very professional, clean, simple, minimalist, bold well designed website
Colors would ideally be greens and blues, cool tones, muted colors, or graytones like:
https://journeybright.org/
Several other clean design examples
http://7harborsrenton.com/
http://www.belvomedical.com/
http://sunpathyouth.com/
http://yourcellduke.com/
I would like the top navigation bar to be able to slide down while browsing site
We are also needing to add several features that are not on our current website:
Questionnaire buttons
Are you toxic questionnaire?
Take our hormone quiz to find out if hormones are affecting your health.
online scheduling option for:
nutrition counselling
testing like body composition, basal metabolic rate, CIMT, breast thermography, VO2 Max testing, Vita Trace
Therapies like whole body vibration, infrared sauna, Exercise with oxygen, hyperbaric oxygen, spinal decompression
Need to have separate page for different services and split up services into:
Consults/Office Visits, Testing, Therapies, Procedures
Need to have a button link to patient portal
Needs to have online store
Need to add navigation button "Start Here"
Need a spot for a video on practice summary
Newsletter signup to collect emails
Testimonials from linkpage
Blog that posts can be shared with social media
Password protected patient access that can integrate into crate.net ideally
Modules for programs online classes/videos
I have attached stock images that you can use, but feel free to find others to use.
I have also attached a copy of our current brochure that shows an overview of the practice
Target Market(s)
Health conscious people of all ages looking for a family medicine doctor
Industry/Entity Type
Alternative Medicine
Coding
Coded - Design and coding required
Number of Pages Required
5+ page
Look and feel

```html
<!DOCTYPE html>
<html lang="en">
<head>
<meta charset="utf-8">
<title>Bright Oak Family Medicine</title>
<link rel="stylesheet" href="https://fonts.googleapis.com/css2?family=Lato:wght@400;700;900&family=Open+Sans:wght@400;600;700&display=swap">
<style>
:root{
  --blue:#3fb4dc;
  --blue-dark:#2a9cc4;
  --green:#8cc63f;
  --green-head:#7cbf3a;
  --ink:#2b2b2b;
  --text:#555;
  --muted:#8a8a8a;
  --grey-bg:#ececec;
  --light-bg:#f7f7f7;
  --white:#fff;
}
*{box-sizing:border-box;margin:0;padding:0}
html,body{width:1200px;height:3614px;overflow:hidden}
body{font-family:"Open Sans",Arial,sans-serif;color:var(--text);background:var(--white);position:relative}
h1,h2,h3,h4{font-family:"Lato",Arial,sans-serif}
.wrap{width:880px;margin:0 auto;position:relative}
section,header,footer{position:relative;overflow:hidden}

/* top bar */
.topbar{height:29px;background:var(--blue);color:var(--white);font-size:11px;font-weight:600}
.topbar .wrap{display:flex;align-items:center;height:29px}
.topbar .item{display:flex;align-items:center;gap:6px;margin-right:30px}
.topbar svg{width:13px;height:13px}
.topbar .account{margin-left:auto;display:flex;gap:8px;align-items:center;letter-spacing:.5px}
.cart{display:flex;align-items:center;gap:4px;margin-left:22px}
.cart .count{background:var(--green);border-radius:8px;font-size:9px;padding:1px 6px}

/* header */
.site-header{height:67px;background:var(--white);border-bottom:1px solid #eee}
.site-header .wrap{display:flex;align-items:center;height:67px}
.brand{display:flex;align-items:center;gap:10px}
.brand-dot{width:30px;height:30px;border-radius:50%;background:var(--green)}
.brand-name{font-family:"Lato",sans-serif;font-weight:900;font-size:22px;color:var(--blue-dark)}
.main-nav{margin-left:auto;display:flex;gap:26px;align-items:center;font-size:12px;font-weight:600;letter-spacing:.6px;color:#555}
.main-nav svg{width:14px;height:14px}

/* hero */
.hero{height:526px}
.hero-photo{position:absolute;inset:0;background:
  radial-gradient(ellipse 22% 40% at 64% 18%,rgba(214,150,40,.85),rgba(214,150,40,0) 70%),
  radial-gradient(ellipse 38% 55% at 80% 45%,rgba(236,244,250,.95),rgba(236,244,250,0) 72%),
  radial-gradient(ellipse 30% 35% at 88% 88%,rgba(70,120,210,.9),rgba(70,120,210,0) 75%),
  radial-gradient(ellipse 30% 40% at 22% 30%,rgba(200,222,236,.75),rgba(200,222,236,0) 70%),
  radial-gradient(ellipse 28% 30% at 30% 95%,rgba(196,110,150,.55),rgba(196,110,150,0) 75%),
  radial-gradient(ellipse 25% 45% at 2% 75%,rgba(230,236,240,.8),rgba(230,236,240,0) 70%),
  linear-gradient(100deg,#4d7f99 0%,#2f6784 35%,#3a80a8 55%,#9fc3dc 80%,#cfe0ec 100%)}
.hero-copy{position:absolute;left:176px;top:370px;color:var(--white)}
.hero-copy h1{font-size:41px;font-weight:900;letter-spacing:.5px;line-height:48px}
.hero-copy p{font-family:"Lato",sans-serif;font-weight:700;font-size:20.5px;margin-top:0}

/* welcome */
.welcome{height:385px}
.welcome-copy{position:absolute;left:0;top:78px;width:460px}
.welcome-copy h2{color:var(--green-head);font-size:36px;font-weight:900;line-height:1}
.welcome-copy h3{color:#333;font-size:19px;font-weight:400;margin-top:4px}
.welcome-copy p{font-size:11px;line-height:15px;margin-top:16px}
.welcome-copy p+p{margin-top:13px}
.btn{display:inline-block;font-family:"Lato",sans-serif;font-weight:700;font-size:12px;letter-spacing:.6px;color:var(--white);border-radius:4px;text-align:center}
.btn-blue{background:var(--blue);padding:9px 18px;margin-top:20px}
.welcome-photo{position:absolute;left:555px;top:77px;width:277px;height:205px;background:
  radial-gradient(ellipse 16% 22% at 56% 25%,rgba(110,170,50,.95),rgba(110,170,50,0) 75%),
  radial-gradient(ellipse 22% 14% at 52% 55%,rgba(80,52,36,.95),rgba(80,52,36,0) 80%),
  radial-gradient(ellipse 48% 32% at 50% 68%,rgba(224,178,150,1),rgba(224,178,150,0) 80%),
  radial-gradient(ellipse 20% 30% at 15% 55%,rgba(230,196,176,.8),rgba(230,196,176,0) 80%),
  radial-gradient(ellipse 20% 30% at 88% 50%,rgba(230,196,176,.8),rgba(230,196,176,0) 80%),
  #fff}

/* section titles */
.section-title{text-align:center;font-size:22px;font-weight:700;color:#333;letter-spacing:1px}

/* services */
.services{height:516px;background:var(--grey-bg)}
.services .section-title{padding-top:36px}
.service-grid{display:flex;justify-content:space-between;margin-top:34px}
.service{width:275px}
.service-photo{height:185px}
.photo-scale{background:
  radial-gradient(ellipse 35% 25% at 35% 20%,rgba(232,190,170,1),rgba(232,190,170,0) 80%),
  radial-gradient(ellipse 30% 22% at 35% 85%,rgba(240,240,240,1),rgba(240,240,240,0) 80%),
  linear-gradient(160deg,#f4f4f4 0%,#dcdcdc 25%,#3c3c3c 45%,#222 65%,#555 100%)}
.photo-caliper{background:
  radial-gradient(ellipse 40% 45% at 70% 65%,rgba(232,180,150,1),rgba(232,180,150,0) 80%),
  radial-gradient(ellipse 35% 55% at 20% 45%,rgba(236,206,186,1),rgba(236,206,186,0) 80%),
  linear-gradient(120deg,#fdfdfd,#f1e3d8)}
.photo-therapy{background:
  radial-gradient(ellipse 25% 22% at 72% 25%,rgba(200,205,210,1),rgba(200,205,210,0) 80%),
  radial-gradient(ellipse 45% 40% at 40% 60%,rgba(232,190,160,1),rgba(232,190,160,0) 80%),
  linear-gradient(160deg,#f5ede6,#ffffff 60%,#eadfd6)}
.service h4{font-size:14px;font-weight:900;letter-spacing:1px;color:#333;margin-top:31px}
.service p{font-size:10.5px;line-height:14px;margin-top:6px}
.btn-green{background:var(--green);padding:8px 16px;margin-top:19px;font-size:11px}

/* blog */
.blog{height:697px;background:linear-gradient(180deg,#4fb2cf,#3aa2c2)}
.blog .section-title{color:var(--white);padding-top:45px}
.section-intro{width:720px;margin:12px auto 0;text-align:center;font-size:10.5px;line-height:14px}
.blog .section-intro{color:#eaf7fb}
.post-list{width:583px;margin:38px 0 0 325px}
.post{display:flex;height:145px;background:var(--white);margin-bottom:16px;box-shadow:0 2px 6px rgba(0,0,0,.2)}
.post-photo{width:200px;background:
  radial-gradient(ellipse 22% 32% at 45% 45%,rgba(150,90,110,.9),rgba(150,90,110,0) 80%),
  radial-gradient(ellipse 60% 30% at 50% 15%,rgba(246,190,110,1),rgba(246,190,110,0) 80%),
  linear-gradient(180deg,#e79a55 0%,#d8793f 40%,#8a5a3a 70%,#4a3a30 100%)}
.post-body{padding:14px 22px 0 30px;flex:1}
.post-body h4{font-size:17px;font-weight:700;color:#333;line-height:20px}
.post-body p{font-size:9.5px;line-height:12px;margin-top:10px}
.read-more{display:block;font-family:"Lato",sans-serif;font-weight:700;font-size:11px;color:var(--green);margin-top:5px}
.see-more{display:block;width:116px;margin:2px 0 0 554px;background:var(--green);padding:8px 0;font-size:12px}

/* testimonials */
.testimonials{height:450px}
.testimonials .section-title{padding-top:32px}
.quotes{position:absolute;top:145px;left:0;width:1200px;height:225px}
.quote{position:absolute;border-radius:10px;background:#e4e4e4;padding:22px 20px 0 48px;font-size:10.5px;line-height:14px;color:#666}
.quote .mark{position:absolute;left:14px;top:16px;font-family:"Lato",serif;font-size:46px;line-height:40px;font-weight:900;color:#444}
.quote:after{content:"";position:absolute;left:50%;bottom:-10px;margin-left:-10px;border:10px solid transparent;border-bottom:0;border-top-color:inherit}
.quote-side{width:243px;height:181px;top:14px;border-top-color:#e4e4e4}
.quote-left{left:171px}
.quote-right{left:786px}
.quote-main{left:458px;width:282px;height:210px;top:0;background:var(--green);color:var(--white);border-top-color:var(--green)}
.quote-main .mark{color:#3c5b1a}
.quote p+p{margin-top:12px}
.arrow{position:absolute;top:84px;width:22px;height:30px}
.arrow-prev{left:96px}
.arrow-next{left:1066px}

/* contact */
.contact{height:463px;background:var(--light-bg)}
.contact .section-title{padding-top:35px}
.contact .lead{text-align:center;font-size:13px;color:#444;margin-top:38px}
.rule{width:40px;height:1px;background:#ccc;margin:20px auto 0}
.contact-form{position:absolute;left:277px;top:200px;width:658px}
.field-row{display:flex;justify-content:space-between}
.field{width:200px;border-bottom:1px solid #ccc;padding-bottom:10px;font-size:9px;letter-spacing:.5px;color:#777}
.field-wide{width:658px;margin-top:75px}
.btn-grey{position:absolute;left:260px;top:150px;width:138px;background:var(--muted);padding:9px 0;font-size:11px}

/* subscribe */
.subscribe{height:137px;background:var(--blue)}
.subscribe h3{text-align:center;color:var(--white);font-size:18px;font-weight:700;padding-top:36px}
.subscribe-form{display:flex;justify-content:center;gap:16px;margin-top:12px}
.sub-input{width:212px;height:31px;background:var(--white);font-size:9px;color:#999;display:flex;align-items:center;gap:6px;padding-left:10px}
.sub-input svg{width:10px;height:10px}
.sub-email{width:200px}
.btn-submit{width:154px;height:31px;background:var(--green);line-height:31px;font-size:13px;letter-spacing:2px;border-radius:0}

/* footer */
.site-footer{height:344px;background:
  radial-gradient(ellipse 40% 30% at 30% 100%,rgba(60,72,84,.6),rgba(60,72,84,0) 80%),
  radial-gradient(ellipse 40% 30% at 75% 100%,rgba(60,72,84,.6),rgba(60,72,84,0) 80%),
  linear-gradient(180deg,#26323c,#1a222a)}
.footer-col{position:absolute;color:#ddd}
.footer-col h4{font-size:13px;font-weight:900;letter-spacing:1px;color:var(--white)}
.col-social{left:169px;top:43px}
.social-widget{width:236px;height:185px;margin-top:22px;background:var(--white);border:1px solid #ccc;padding:8px}
.widget-banner{height:110px;background:
  radial-gradient(ellipse 30% 40% at 25% 60%,rgba(230,200,180,.9),rgba(230,200,180,0) 80%),
  radial-gradient(ellipse 30% 40% at 75% 40%,rgba(180,200,220,.9),rgba(180,200,220,0) 80%),
  linear-gradient(135deg,#dfe6ea,#9bb1c0)}
.widget-row{display:flex;gap:6px;margin-top:10px}
.widget-row span{height:24px;flex:1;background:linear-gradient(135deg,#c9b5a5,#8aa2b4)}
.col-info{left:441px;top:43px}
.col-info ul{list-style:none;margin-top:20px}
.col-info li{font-size:10.5px;line-height:22px;padding-left:18px;position:relative}
.col-info li:before{content:"";position:absolute;left:2px;top:9px;width:4px;height:4px;background:#ddd}
.col-contact{left:807px;top:52px}
.col-contact .brand-name{color:var(--blue);font-size:22px}
.col-contact .brand-dot{width:26px;height:26px}
.contact-list{list-style:none;margin-top:26px}
.contact-list li{display:flex;align-items:center;gap:12px;font-size:10.5px;height:26px}
.contact-list svg{width:12px;height:12px}
.follow{font-size:10px;letter-spacing:1.5px;font-weight:700;margin-top:17px}
.social-row{display:flex;gap:16px;margin-top:14px}
.social-row span{width:28px;height:28px;border-radius:50%;background:var(--green)}
.copyright{position:absolute;right:155px;bottom:8px;font-size:9px;color:#bbb}
</style>
</head>
<body>

<div class="topbar">
  <div class="wrap">
    <div class="item"><svg viewBox="0 0 24 24" fill="#fff"><path d="M6.6 10.8a15 15 0 0 0 6.6 6.6l2.2-2.2a1 1 0 0 1 1-.25 11 11 0 0 0 3.6.6 1 1 0 0 1 1 1V20a1 1 0 0 1-1 1A17 17 0 0 1 3 4a1 1 0 0 1 1-1h3.5a1 1 0 0 1 1 1 11 11 0 0 0 .6 3.6 1 1 0 0 1-.25 1z"/></svg>(806) 555-0142</div>
    <div class="item"><svg viewBox="0 0 24 24" fill="#fff"><path d="M2 5h20v14H2z M2 5l10 8 10-8" stroke="#3fb4dc" stroke-width="1.5"/></svg>support@brightoak.com</div>
    <div class="item"><svg viewBox="0 0 24 24"><circle cx="12" cy="12" r="10" fill="#fff"/><path d="M12 6v6l4 2" stroke="#3fb4dc" stroke-width="2" fill="none"/></svg>Mon - Sat 9:00 - 19:00</div>
    <div class="account"><span>LOGIN</span><span>/</span><span>REGISTER</span>
      <span class="cart"><svg viewBox="0 0 24 24" fill="none" stroke="#fff" stroke-width="2"><path d="M2 3h3l3 12h11l2-8H6"/><circle cx="9" cy="20" r="1.5"/><circle cx="18" cy="20" r="1.5"/></svg><span class="count">0</span></span>
    </div>
  </div>
</div>

<header class="site-header">
  <div class="wrap">
    <div class="brand"><span class="brand-dot"></span><span class="brand-name">Bright Oak Family Medicine</span></div>
    <nav class="main-nav">
      <span>HOME</span><span>ABOUT</span><span>SERVICES</span><span>TESTIMONIALS</span><span>BLOG</span><span>CONTACT</span>
      <svg viewBox="0 0 24 24" fill="none" stroke="#333" stroke-width="3"><circle cx="10" cy="10" r="7"/><path d="M15 15l7 7"/></svg>
    </nav>
  </div>
</header>

<section class="hero">
  <div class="hero-photo" role="img" aria-label="Laboratory photo: gloved hand using a pipette over a sample tray, molecule diagram in the background"></div>
  <div class="hero-copy">
    <h1>Are you aware of your toxicity level?</h1>
    <p>Let us help you find. Take the questionaire today! TAKE TEST</p>
  </div>
</section>

<section class="welcome">
  <div class="wrap">
    <div class="welcome-copy">
      <h2>WELCOME TO BRIGHT OAK</h2>
      <h3>Restoring your Health Naturally</h3>
      <p>Nemo enim ipsam voluptatem quia voluptas sit aspernatur aut odit aut fugit, sed quia consequuntur magni dolores eos qui ratione voluptatem sequi nesciunt. Neque porro quisquam est, qui dolorem ipsum quia dolor sit amet, consectetur, adipisci velit.</p>
      <p>sed quia non numquam eius modi tempora incidunt ut labore et dolore magnam aliquam quaerat voluptatem. Ut enim ad minima veniam, quis nostrum exercitationem ullam corporis suscipit laboriosam, nisi ut aliquid ex ea commodi consequatur?</p>
      <span class="btn btn-blue">KNOW MORE</span>
    </div>
    <div class="welcome-photo" role="img" aria-label="Cupped hands holding soil with a green seedling"></div>
  </div>
</section>

<section class="services">
  <h2 class="section-title">OUR SERVICES</h2>
  <div class="wrap service-grid">
    <article class="service">
      <div class="service-photo photo-scale" role="img" aria-label="Bare feet stepping onto a bathroom scale"></div>
      <h4>MODALITIES</h4>
      <p>Nemo enim ipsam voluptatem quia voluptas sit aspernatur aut odit aut fugit, sed quia consequuntur magni dolores eos qui ratione voluptatem sequi nesciunt. Neque porro quisquam est, qui dolorem ipsum quia dolor sit amet, consectetur, adipisci velit.</p>
      <span class="btn btn-green">KNOW MORE</span>
    </article>
    <article class="service">
      <div class="service-photo photo-caliper" role="img" aria-label="Skin testing with a caliper on an upper arm"></div>
      <h4>TESTING</h4>
      <p>Nemo enim ipsam voluptatem quia voluptas sit aspernatur aut odit aut fugit, sed quia consequuntur magni dolores eos qui ratione voluptatem sequi nesciunt. Neque porro quisquam est, qui dolorem ipsum quia dolor sit amet, consectetur, adipisci velit.</p>
      <span class="btn btn-green">KNOW MORE</span>
    </article>
    <article class="service">
      <div class="service-photo photo-therapy" role="img" aria-label="Body therapy device applied to the abdomen"></div>
      <h4>THERAPIES</h4>
      <p>Nemo enim ipsam voluptatem quia voluptas sit aspernatur aut odit aut fugit, sed quia consequuntur magni dolores eos qui ratione voluptatem sequi nesciunt. Neque porro quisquam est, qui dolorem ipsum quia dolor sit amet, consectetur, adipisci velit.</p>
      <span class="btn btn-green">KNOW MORE</span>
    </article>
  </div>
</section>

<section class="blog">
  <h2 class="section-title">BLOG</h2>
  <p class="section-intro">Nemo enim ipsam voluptatem quia voluptas sit aspernatur aut odit aut fugit, sed quia consequuntur magni dolores eos qui ratione voluptatem sequi nesciunt. Neque porro quisquam est, qui dolorem ipsum quia dolor sit amet, consectetur, adipisci velit.</p>
  <div class="post-list">
    <article class="post">
      <div class="post-photo" role="img" aria-label="Yoga pose outdoors at sunset"></div>
      <div class="post-body">
        <h4>Yoga is Possible for Anyone Who Really Wants It</h4>
        <p>Nemo enim ipsam voluptatem quia voluptas sit aspernatur aut odit aut fugit, sed quia consequuntur magni dolores eos qui ratione voluptatem sequi nesciunt. Neque porro quisquam est, qui dolorem ipsum quia dolor sit amet, consectetur, adipisci velit.</p>
        <span class="read-more">READ MORE</span>
      </div>
    </article>
    <article class="post">
      <div class="post-photo" role="img" aria-label="Yoga pose outdoors at sunset"></div>
      <div class="post-body">
        <h4>Yoga is Possible for Anyone Who Really Wants It</h4>
        <p>Nemo enim ipsam voluptatem quia voluptas sit aspernatur aut odit aut fugit, sed quia consequuntur magni dolores eos qui ratione voluptatem sequi nesciunt. Neque porro quisquam est, qui dolorem ipsum quia dolor sit amet, consectetur, adipisci velit.</p>
        <span class="read-more">READ MORE</span>
      </div>
    </article>
    <article class="post">
      <div class="post-photo" role="img" aria-label="Yoga pose outdoors at sunset"></div>
      <div class="post-body">
        <h4>Yoga is Possible for Anyone Who Really Wants It</h4>
        <p>Nemo enim ipsam voluptatem quia voluptas sit aspernatur aut odit aut fugit, sed quia consequuntur magni dolores eos qui ratione voluptatem sequi nesciunt. Neque porro quisquam est, qui dolorem ipsum quia dolor sit amet, consectetur, adipisci velit.</p>
        <span class="read-more">READ MORE</span>
      </div>
    </article>
  </div>
  <span class="btn see-more">SEE MORE</span>
</section>

<section class="testimonials">
  <h2 class="section-title">TESTIMONIALS</h2>
  <p class="section-intro">Nemo enim ipsam voluptatem quia voluptas sit aspernatur aut odit aut fugit, sed quia consequuntur magni dolores eos qui ratione voluptatem sequi nesciunt. Neque porro quisquam est, qui dolorem ipsum quia dolor sit amet, consectetur, adipisci velit.</p>
  <div class="quotes">
    <svg class="arrow arrow-prev" viewBox="0 0 22 30" fill="none" stroke="#bbb" stroke-width="2"><path d="M16 3L5 15l11 12"/></svg>
    <blockquote class="quote quote-side quote-left"><span class="mark">&ldquo;</span>
      <p>Nemo enim ipsam voluptatem quia voluptas sit aspernatur aut odit aut fugit, sed quia consequuntur magni dolores eos qui ratione voluptatem sequi nesciunt. Neque porro quisquam est, qui dolorem ipsum quia dolor sit amet, consectetur, adipisci velit.</p>
    </blockquote>
    <blockquote class="quote quote-main"><span class="mark">&ldquo;</span>
      <p>Nemo enim ipsam voluptatem quia voluptas sit aspernatur aut odit aut fugit, sed quia consequuntur magni dolores eos qui ratione voluptatem sequi nesciunt. Neque porro quisquam est, qui dolorem ipsum quia dolor sit amet, consectetur, adipisci velit.</p>
      <p>Neque porro quisquam est, qui dolorem ipsum quia dolor sit amet, consectetur, adipisci velit.</p>
    </blockquote>
    <blockquote class="quote quote-side quote-right"><span class="mark">&ldquo;</span>
      <p>Nemo enim ipsam voluptatem quia voluptas sit aspernatur aut odit aut fugit, sed quia consequuntur magni dolores eos qui ratione voluptatem sequi nesciunt. Neque porro quisquam est, qui dolorem ipsum quia dolor sit amet, consectetur, adipisci velit.</p>
    </blockquote>
    <svg class="arrow arrow-next" viewBox="0 0 22 30" fill="none" stroke="#bbb" stroke-width="2"><path d="M6 3l11 12L6 27"/></svg>
  </div>
</section>

<section class="contact">
  <h2 class="section-title">CONTACT US</h2>
  <p class="lead">For any questions on our services or products, please fill in the form below &amp; we will be glad to assist you.</p>
  <div class="rule"></div>
  <form class="contact-form">
    <div class="field-row">
      <div class="field">YOUR NAME</div>
      <div class="field">YOUR EMAIL</div>
      <div class="field">SUBJECT</div>
    </div>
    <div class="field field-wide">YOUR MESSAGE</div>
    <span class="btn btn-grey">SEND MESSAGE</span>
  </form>
</section>

<section class="subscribe">
  <h3>Have Questions ? Feel free to Subscribe for Latest News &amp; Updates.</h3>
  <div class="subscribe-form">
    <div class="sub-input"><svg viewBox="0 0 10 10" fill="#999"><circle cx="5" cy="3" r="2.3"/><path d="M0.5 10a4.5 4 0 0 1 9 0z"/></svg>Full Name</div>
    <div class="sub-input sub-email"><svg viewBox="0 0 10 10" fill="none" stroke="#999"><rect x="0.5" y="1.5" width="9" height="7"/><path d="M0.5 1.5l4.5 4 4.5-4"/></svg>Email Address</div>
    <span class="btn btn-submit">SUBMIT</span>
  </div>
</section>

<footer class="site-footer" role="img" aria-label="Dim city skyline backdrop">
  <div class="footer-col col-social">
    <h4>LIKE US ON LINKPAGE</h4>
    <div class="social-widget">
      <div class="widget-banner" role="img" aria-label="Page cover photo"></div>
      <div class="widget-row"><span></span><span></span><span></span><span></span><span></span></div>
    </div>
  </div>
  <div class="footer-col col-info">
    <h4>INFORMATION</h4>
    <ul>
      <li>Services</li><li>About Us</li><li>Forum</li><li>Help center</li><li>FAQ</li><li>Privacy Policy</li><li>Resources</li><li>Contact</li>
    </ul>
  </div>
  <div class="footer-col col-contact">
    <div class="brand"><span class="brand-dot"></span><span class="brand-name">Bright Oak</span></div>
    <ul class="contact-list">
      <li><svg viewBox="0 0 24 24" fill="#ddd"><path d="M12 2a7 7 0 0 0-7 7c0 5 7 13 7 13s7-8 7-13a7 7 0 0 0-7-7zm0 9.5A2.5 2.5 0 1 1 12 6.5a2.5 2.5 0 0 1 0 5z"/></svg>4410 Linden Ave, Fairview, TX 79100</li>
      <li><svg viewBox="0 0 24 24" fill="#ddd"><path d="M2 5h20v14H2z"/><path d="M2 5l10 8 10-8" stroke="#1f2831" stroke-width="2" fill="none"/></svg>info@brightoak.com</li>
      <li><svg viewBox="0 0 24 24" fill="#ddd"><path d="M6.6 10.8a15 15 0 0 0 6.6 6.6l2.2-2.2a1 1 0 0 1 1-.25 11 11 0 0 0 3.6.6 1 1 0 0 1 1 1V20a1 1 0 0 1-1 1A17 17 0 0 1 3 4a1 1 0 0 1 1-1h3.5a1 1 0 0 1 1 1 11 11 0 0 0 .6 3.6 1 1 0 0 1-.25 1z"/></svg>(806) 555-0142</li>
    </ul>
    <p class="follow">FOLLOW US</p>
    <div class="social-row"><span></span><span></span><span></span><span></span><span></span></div>
  </div>
  <p class="copyright">Copyright &copy; 2016. Rights Reserved.</p>
</footer>

</body>
</html>
```